IT services company needs a business card designed

-2 sided business card.-Front is going to be the logo raised (3D floating effect) on a black background. Make the logos spider web shiny silver and keep the spider the same design. -Back needs to have the following information:Darrel Sotho, Managing Partner, Cell: 738-402-1954, Website: Plankhorn.com, Email: Darrel@Plankhorn.com
Target Market(s)
IT Services
Industry/Entity Type
It Company
Contact Information for Business Card
-2 sided business card.
-Front is going to be the logo raised (3D floating effect) on a black background. Make the logos spider web shiny silver and keep the spider the same design.
-Back needs to have the following information:
Darrel Sotho, Managing Partner, Cell: 738-402-1954, Website: Plankhorn.com, Email: Darrel@Plankhorn.com

```html
<!DOCTYPE html>
<html lang="en">
<head>
<meta charset="utf-8">
<title>Plankhorn — Business Card</title>
<link rel="stylesheet" href="https://fonts.googleapis.com/css2?family=Lato:wght@400;700&display=swap">
<style>
  :root {
    --page-bg: #e4e4e6;
    --card-bg: #f6f5f5;
    --ink-dark: #2b2b2b;
    --ink-body: #3a3a3a;
    --accent-blue: #1a9ee6;
    --mark-tint: #bfe0f3;
    --web-blue: #8ccbef;
    --web-grey: #c9cdd1;
  }
  html, body {
    margin: 0;
    width: 1200px;
    height: 900px;
    overflow: hidden;
    background: var(--page-bg);
    font-family: "Lato", sans-serif;
  }
  .card {
    position: absolute;
    left: 100px;
    top: 140px;
    width: 1000px;
    height: 620px;
    background: var(--card-bg);
    box-shadow: 0 10px 30px rgba(0,0,0,0.12);
    overflow: hidden;
  }
  .brand-mark {
    position: absolute;
    left: 106px;
    top: 74px;
    width: 116px;
    height: 116px;
    border-radius: 50%;
    background: var(--mark-tint);
  }
  .brand-name {
    position: absolute;
    left: 56px;
    top: 256px;
    margin: 0;
    font-size: 38px;
    font-weight: 400;
    letter-spacing: 3px;
    color: var(--ink-dark);
  }
  .person-name {
    position: absolute;
    left: 54px;
    top: 353px;
    margin: 0;
    font-size: 35px;
    font-weight: 700;
    color: var(--accent-blue);
    letter-spacing: 0.5px;
  }
  .person-role {
    position: absolute;
    left: 54px;
    top: 394px;
    margin: 0;
    font-size: 27px;
    color: var(--ink-body);
  }
  .contact-list {
    position: absolute;
    left: 54px;
    top: 454px;
    margin: 0;
    padding: 0;
    list-style: none;
    font-size: 27px;
    color: var(--ink-body);
  }
  .contact-list li {
    display: flex;
    align-items: center;
    height: 37px;
  }
  .contact-icon {
    width: 22px;
    height: 22px;
    margin-right: 10px;
    fill: var(--accent-blue);
  }
  .web-artwork {
    position: absolute;
    left: 567px;
    top: 0;
    width: 433px;
    height: 620px;
    border-radius: 60% 0 0 60% / 50% 0 0 50%;
    background:
      radial-gradient(ellipse 45% 55% at 100% 42%, rgba(26,158,230,0.75) 0%, rgba(26,158,230,0.35) 55%, transparent 100%),
      linear-gradient(180deg, var(--web-blue) 0%, #dcebf5 48%, #e3e5e7 55%, var(--web-grey) 100%);
  }
</style>
</head>
<body>
  <div class="card">
    <div class="brand-mark" aria-hidden="true"></div>
    <p class="brand-name">PLANKHORN</p>

    <h1 class="person-name">DARREL SOTHO</h1>
    <p class="person-role">Managing Partner</p>

    <ul class="contact-list">
      <li>
        <svg class="contact-icon" viewBox="0 0 24 24" aria-hidden="true"><path d="M6.6 10.8a15.1 15.1 0 0 0 6.6 6.6l2.2-2.2a1 1 0 0 1 1-.25 11.4 11.4 0 0 0 3.6.57 1 1 0 0 1 1 1V20a1 1 0 0 1-1 1A17 17 0 0 1 3 4a1 1 0 0 1 1-1h3.5a1 1 0 0 1 1 1c0 1.25.2 2.45.57 3.57a1 1 0 0 1-.25 1z"/></svg>
        738-402-1954
      </li>
      <li>
        <svg class="contact-icon" viewBox="0 0 24 24" aria-hidden="true"><rect x="2" y="5" width="20" height="14"/><path d="M3 6l9 7 9-7" fill="none" stroke="#fff" stroke-width="1.6"/></svg>
        Darrel@Plankhorn.com
      </li>
      <li>
        <svg class="contact-icon" viewBox="0 0 24 24" aria-hidden="true"><circle cx="12" cy="12" r="10"/><ellipse cx="12" cy="12" rx="4" ry="10" fill="none" stroke="#fff" stroke-width="1.4"/><path d="M2 12h20" stroke="#fff" stroke-width="1.4"/></svg>
        www.Plankhorn.com
      </li>
    </ul>

    <div class="web-artwork" role="img" aria-label="Illustration of a blue and grey spider web with a faceted blue spider climbing the right edge"></div>
  </div>
</body>
</html>
```